Business Card - Rebranding for Consulting Firm

We are renaming and rebranding our consulting firm and need to raise the level of quality of our cards as part of that effort. We consult to leading high tech, life science and other innovation sector companies.

Need a two-sided business card design.

Side 1: (a) Company logo (b) tag line: Invest Wisely in the People You Lead (c) Name (d) Title (e) Phone 1: Office (f) Phone 2: Mobile (g) email: person@HollowmereAdvisory.com

Side 2: Two lines of text: (a) Vision Sets Direction. Markets Keep Moving. People Deliver Results. (b) We help you master all three.

Target Market(s)

Business and human resources executives and senior managers

Industry/Entity Type

Management Consulting

Contact Information for Business Card

Font styles to use
Sans Serif

Requirements
Must have
• clean, not too busy, but with a bit of creativity. Stick to the colors used in the attached logo
• appeal to high tech, life science companies
Nice to have
• prefer white background

```html
<!DOCTYPE html>
<html lang="en">
<head>
<meta charset="utf-8">
<title>Hollowmere Advisory – Business Cards</title>
<link href="https://fonts.googleapis.com/css2?family=Heebo:wght@300;400;700&display=swap" rel="stylesheet">
<style>
  :root{
    --backdrop:#e7d2c4;
    --card-light:#ececee;
    --card-dark:#1b1b1b;
    --brand-blue:#1a6aa6;
    --brand-bright:#1f86c8;
    --ink:#1d1d1d;
    --muted:#c9c9c9;
    --rule-light:#8a8a8a;
    --rule-dark:#5a5a5a;
  }
  *{box-sizing:border-box;margin:0;padding:0}
  html,body{width:1200px;height:774px;overflow:hidden;background:var(--backdrop)}
  body{font-family:"Heebo",Arial,sans-serif;position:relative}
  .card-sheet{
    position:absolute;left:150px;top:124px;width:910px;height:522px;
    display:grid;grid-template-columns:455px 455px;grid-template-rows:261px 261px;
  }
  .card{position:relative;overflow:hidden}
  .card--back{background:var(--card-light)}
  .card--front{background:var(--card-dark);color:var(--muted)}

  /* back side */
  .wordmark{
    position:absolute;left:0;right:0;top:76px;text-align:center;
    font-weight:400;font-size:36px;letter-spacing:-0.5px;color:var(--brand-blue);
    display:flex;align-items:center;justify-content:center;gap:12px;
  }
  .wordmark__square{width:18px;height:18px;background:var(--brand-blue)}
  .motto{position:absolute;right:62px;top:202px;width:340px;color:var(--ink);font-size:11px;text-align:right}
  .motto__line{display:block;line-height:19px;white-space:nowrap}
  .motto__rule{position:absolute;left:0;top:27px;width:178px;border-top:1px solid var(--rule-light)}

  /* front side */
  .person{position:absolute;left:31px;top:42px}
  .person__name{font-weight:700;font-size:18px;color:var(--brand-bright);line-height:20px}
  .person__title{font-weight:300;font-size:12.5px;line-height:16px}
  .brand-square{position:absolute;right:52px;top:30px;width:40px;height:40px;background:var(--brand-bright)}
  .short-rule{position:absolute;left:31px;top:106px;width:36px;border-top:1px solid var(--rule-dark)}
  .address{position:absolute;left:31px;top:138px;font-weight:300;font-size:12px;line-height:15.5px;font-style:normal}
  .address__company{color:var(--brand-bright)}
  .contacts{position:absolute;left:202px;top:138px;font-weight:300;font-size:12px;line-height:15.5px;list-style:none}
  .contacts li{display:flex;align-items:center;gap:6px;white-space:nowrap}
  .contacts svg{width:9px;height:9px;fill:var(--brand-bright)}
  .tagline{position:absolute;left:31px;right:62px;top:218px;display:flex;align-items:center;gap:12px;font-weight:300;font-size:10.5px}
  .tagline span:first-child{white-space:nowrap}
  .tagline__rule{flex:1;border-top:1px solid var(--rule-dark)}
</style>
</head>
<body>
<main class="card-sheet">

  <section class="card card--back">
    <div class="wordmark"><span class="wordmark__square"></span>Hollowmere Advisory</div>
    <div class="motto">
      <span class="motto__line">Vision Sets Direction. Markets Keep Moving. People Deliver Results.</span>
      <span class="motto__line">We help you master all three.</span>
      <span class="motto__rule"></span>
    </div>
  </section>

  <section class="card card--front">
    <div class="person">
      <p class="person__name">Alex Morgan</p>
      <p class="person__title">Marketing Director</p>
    </div>
    <span class="brand-square"></span>
    <span class="short-rule"></span>
    <address class="address">
      <span class="address__company">Hollowmere Advisory</span><br>
      18 Larkspur Lane<br>P.O. Box 2210<br>Fairview, NJ 07022
    </address>
    <ul class="contacts">
      <li><svg viewBox="0 0 10 10"><path d="M2.5 0h5v10h-5zM3.3 1v7h3.4V1z"/></svg>000 000 0000</li>
      <li><svg viewBox="0 0 10 10"><path d="M2 0l2 2.5-1 1.2a6 6 0 0 0 3.3 3.3l1.2-1L10 8l-1.5 2C4 10 0 6 0 1.5z"/></svg>000 000 0000</li>
      <li><svg viewBox="0 0 10 10"><path d="M0 2h10v6H0zM1 3l4 2.6L9 3v-.2H1z"/></svg>person@HollowmereAdvisory.com</li>
      <li><svg viewBox="0 0 10 10"><path d="M5 0a5 5 0 1 0 0 10A5 5 0 0 0 5 0zm0 1.2a3.8 3.8 0 1 1 0 7.6 3.8 3.8 0 0 1 0-7.6z"/></svg>www.hollowmereadvisory.com</li>
    </ul>
    <div class="tagline"><span>Invest Wisely in the People You Lead</span><span class="tagline__rule"></span></div>
  </section>

  <section class="card card--front">
    <div class="person">
      <p class="person__name">Alex Morgan</p>
      <p class="person__title">Marketing Director</p>
    </div>
    <span class="brand-square"></span>
    <span class="short-rule"></span>
    <address class="address">
      <span class="address__company">Hollowmere Advisory</span><br>
      18 Larkspur Lane<br>P.O. Box 2210<br>Fairview, NJ 07022
    </address>
    <ul class="contacts">
      <li><svg viewBox="0 0 10 10"><path d="M2.5 0h5v10h-5zM3.3 1v7h3.4V1z"/></svg>000 000 0000</li>
      <li><svg viewBox="0 0 10 10"><path d="M2 0l2 2.5-1 1.2a6 6 0 0 0 3.3 3.3l1.2-1L10 8l-1.5 2C4 10 0 6 0 1.5z"/></svg>000 000 0000</li>
      <li><svg viewBox="0 0 10 10"><path d="M0 2h10v6H0zM1 3l4 2.6L9 3v-.2H1z"/></svg>person@HollowmereAdvisory.com</li>
      <li><svg viewBox="0 0 10 10"><path d="M5 0a5 5 0 1 0 0 10A5 5 0 0 0 5 0zm0 1.2a3.8 3.8 0 1 1 0 7.6 3.8 3.8 0 0 1 0-7.6z"/></svg>www.hollowmereadvisory.com</li>
    </ul>
    <div class="tagline"><span>Invest Wisely in the People You Lead</span><span class="tagline__rule"></span></div>
  </section>

  <section class="card card--back">
    <div class="wordmark"><span class="wordmark__square"></span>Hollowmere Advisory</div>
    <div class="motto">
      <span class="motto__line">Vision Sets Direction. Markets Keep Moving. People Deliver Results.</span>
      <span class="motto__line">We help you master all three.</span>
      <span class="motto__rule"></span>
    </div>
  </section>

</main>
</body>
</html>
```